Daylight9 | An Alcolohism Recovery Blogging Site

Daylight9.com.au is a blog based on alcoholism. Primarily, alcholics who are in sobreity, or recovery. The blog posts are centred around this and are written by other alcholics who share their thoughts, strenght, experience, thoeries on how to get sober, and stay sober, but primarily, live a better life in active sobriety. The site provides information related to KF and other services/groups that assist in alcolohism. We write E-Books and sell these also. Daylight9 strives to be a blog that alcoholics want to read, and get strength and hope from reading it, and the posts from other users. We want to be easy to use, simple to navigate and sharply designed. We want the site to be cutting edge and appealing. We want to engage the audience from the first moment they hit the page, no matter where they land. I like this website as a model for a wordpress site making good use of simplicity = thriftcompass.com.au

Target Market(s)

People who might think they have a problem with Alcohol, people who are alcholics looking at entering rehab or recovery, people that are alcoholics in recovery already

Requirements
Must have
• simplicity, large fonts for headings, space for advertising through ad words and other forms, nice large navigation across the top, a sharp, html 5 feel, i want to be using great fonts and nice/sheek.
Nice to have
• logo will be used in print as well as online. It would be VERY GOOD to have someone design a ecover for my ebook i will be selling on this website. the book is titled "THE CHOICE TO PUT DOWN YOUR GLASS - The Clear Path toward finding calm and keeping it there!"
Should not have
• do not include illustrations of alcohol.

```html
<!DOCTYPE html>
<html lang="en">
<head>
<meta charset="utf-8">
<title>Daylight9 | Getting back on track</title>
<link rel="stylesheet" href="https://fonts.googleapis.com/css2?family=PT+Sans:wght@400;700&family=Noto+Sans:wght@400&family=Comfortaa:wght@400&display=swap">
<style>
  :root {
    --page-cream: #efe9bd;
    --header-dark: #3a3a3c;
    --header-mid: #5e5e60;
    --panel-grey: #9d9d9f;
    --bar-top: #55555f;
    --bar-bottom: #32323b;
    --gold: #f2c14e;
    --gold-link: #c99a1e;
    --box-top: #ffffff;
    --box-bottom: #e4e4e6;
    --box-edge: #5d5d63;
    --ink: #222226;
    --title-blue: #3f4b70;
    --nav-text: #ffffff;
  }
  * { box-sizing: border-box; margin: 0; padding: 0; }
  html, body { width: 1095px; height: 1200px; overflow: hidden; }
  body {
    position: relative;
    background: var(--page-cream);
    font-family: "Noto Sans", Verdana, sans-serif;
    color: var(--ink);
  }
  .site-header {
    position: absolute; left: 0; top: 0; width: 1095px; height: 233px;
    background: radial-gradient(ellipse at 40% 40%, var(--header-mid), var(--header-dark) 75%);
  }
  .brand { position: absolute; left: 34px; top: 70px; display: flex; align-items: center; gap: 14px; }
  .brand-dot { width: 62px; height: 62px; border-radius: 50%; background: var(--gold); }
  .brand-name { font-family: "PT Sans", sans-serif; font-weight: 700; font-size: 66px; color: var(--gold); line-height: 1; }
  .tagline {
    position: absolute; left: 357px; top: 162px;
    font-family: "Comfortaa", sans-serif; font-size: 36px; letter-spacing: 1px; color: #e4e4e4;
  }
  .footer-band {
    position: absolute; left: 0; top: 1140px; width: 1095px; height: 60px;
    background: linear-gradient(#4a4a4c, var(--header-dark));
  }
  .main-panel {
    position: absolute; left: 89px; top: 211px; width: 911px; height: 920px;
    background: var(--panel-grey); border-radius: 10px;
    box-shadow: 0 3px 8px rgba(0,0,0,.45);
  }
  .main-nav {
    position: absolute; left: 89px; top: 211px; width: 911px; height: 47px;
    background: linear-gradient(var(--bar-top), var(--bar-bottom));
    border-radius: 10px 10px 0 0;
  }
  .main-nav a {
    position: absolute; top: 12px; font-family: "PT Sans", sans-serif;
    font-size: 19px; color: var(--nav-text); text-decoration: none;
  }
  .main-nav a.is-current { color: var(--gold); }
  .search { position: absolute; left: 713px; top: 10px; display: flex; }
  .search-field {
    width: 141px; height: 26px; background: #fff; border-radius: 3px 0 0 3px;
    font-size: 13px; color: #8a8a8a; padding: 5px 0 0 13px; font-family: "PT Sans", sans-serif;
  }
  .search-button {
    width: 30px; height: 26px; background: linear-gradient(#b8b8b8, #8d8d8d);
    border-radius: 0 3px 3px 0; display: flex; align-items: center; justify-content: center;
  }
  .box {
    position: absolute; border: 2px solid var(--box-edge); border-radius: 10px;
    background: linear-gradient(var(--box-top), var(--box-bottom));
    box-shadow: 0 3px 5px rgba(0,0,0,.35); overflow: hidden;
  }
  .box-title {
    height: 47px; background: linear-gradient(var(--bar-top), var(--bar-bottom));
    color: var(--gold); font-family: "PT Sans", sans-serif; font-size: 27px; font-weight: 400;
    padding: 5px 0 0 14px;
  }
  .abs { position: absolute; }
  .body-copy { font-size: 13px; line-height: 22px; }
  .post-title { font-family: "PT Sans", sans-serif; font-weight: 400; font-size: 33px; color: var(--title-blue); left: 12px; }
  .post-meta { font-size: 12px; left: 12px; }
  .post-meta a { color: var(--gold-link); text-decoration: none; }
  .post-photo {
    left: 11px; top: 149px; width: 157px; height: 159px; border: 3px solid #111;
    background: linear-gradient(#dfe6ee, #b9c6d6);
  }
  .button {
    display: flex; align-items: center; justify-content: center;
    background: linear-gradient(#5c5c68, #34343e); border-radius: 7px;
    color: var(--gold); font-family: "PT Sans", sans-serif; text-decoration: none;
    box-shadow: 0 2px 3px rgba(0,0,0,.4);
  }
  .read-more { width: 109px; height: 29px; font-size: 14px; }
  .share-icons { display: flex; gap: 6px; left: 12px; }
  .share-icons span { width: 21px; height: 21px; border-radius: 3px; }
  .share-feed { background: #e8791e; }
  .share-one { background: #3b5998; }
  .share-two { background: #2f8fd1; }
  .ebook-quote { left: 14px; top: 58px; width: 270px; font-size: 15px; line-height: 21px; color: #333; }
  .ebook-cover {
    left: 17px; top: 148px; width: 255px; height: 126px; border: 1px solid #aaa; border-radius: 8px;
    background: linear-gradient(#e6e6e6, #bdbdbd);
  }
  .download { left: 75px; top: 287px; width: 207px; height: 34px; font-size: 20px; }
  .link-col { font-size: 12px; }
  .link-col h3 { font-weight: 400; font-size: 14px; text-decoration: underline; color: #000; margin-bottom: 6px; }
  .link-col a { display: block; color: var(--gold-link); line-height: 22px; margin-left: 8px; }
</style>
</head>
<body>
  <header class="site-header" role="img" aria-label="Dark stone texture header with scattered footprint decoration">
    <div class="brand"><span class="brand-dot"></span><span class="brand-name">Daylight9</span></div>
    <div class="tagline">Getting back on track</div>
  </header>

  <div class="main-panel"></div>
  <nav class="main-nav">
    <a class="is-current" href="#" style="left:24px">Home</a>
    <a href="#" style="left:123px">About Us</a>
    <a href="#" style="left:255px">Contact Us</a>
    <div class="search">
      <div class="search-field">Search</div>
      <div class="search-button">
        <svg width="16" height="16" viewBox="0 0 16 16"><circle cx="6.5" cy="6.5" r="4.5" fill="none" stroke="#fff" stroke-width="2"/><line x1="10" y1="10" x2="14.5" y2="14.5" stroke="#fff" stroke-width="2.4" stroke-linecap="round"/></svg>
      </div>
    </div>
  </nav>

  <section class="box welcome" style="left:105px;top:276px;width:575px;height:175px">
    <h2 class="box-title">Welcome</h2>
    <p class="abs body-copy" style="left:15px;top:65px;width:530px">Lorem ipsum dolor sit amet, consectetur adipiscing elit. Phasellus ornare venenatis rhoncus. Nullam ac massa ipsum. Ut vel nisl nisl. Nam et tellus justo. Pellentesque ut mollis est. Sed porta diam nec risus egestas mollis. Duis vestibulum felis at dui eleifend id posuere risus vulputate. Nulla mi elit, tempus sed iaculis a, fermentum at orci.</p>
  </section>

  <section class="box blog" style="left:105px;top:468px;width:575px;height:620px">
    <h2 class="box-title">Blog</h2>
    <article>
      <h3 class="abs post-title" style="top:56px">September 27th - October</h3>
      <p class="abs post-meta" style="top:120px">Posted by <a href="#">admin</a> on Sep27 2010 | <a href="#">1 comment</a></p>
      <div class="abs post-photo" role="img" aria-label="Photo of a smiling couple"></div>
      <p class="abs body-copy" style="left:180px;top:144px;width:350px">luctus elementum. Vivamus eu purus a magna adipiscing gravida. Cras orci nulla, rhoncus ac viverra sed, volutpat nec massa. Curabitur dapibus, tellus ut molestie ornare, diam sem sagittis sapien, facilisis dictum ligula velit ut neque. Donec in magna sit amet leo mollis sagittis id sed odio.</p>
      <a class="abs button read-more" href="#" style="left:438px;top:277px">Read more</a>
      <div class="abs share-icons" style="top:320px"><span class="share-feed"></span><span class="share-one"></span><span class="share-two"></span></div>
    </article>
    <article>
      <h3 class="abs post-title" style="top:347px">September 23th - October</h3>
      <p class="abs post-meta" style="top:411px">Posted by <a href="#">admin</a> on Sep23 2010 | <a href="#">1 comment</a></p>
      <p class="abs body-copy" style="left:12px;top:438px;width:545px">luctus elementum. Vivamus eu purus a magna adipiscing gravida. Cras orci nulla, rhoncus ac viverra sed, volutpat nec massa. Curabitur dapibus, tellus ut molestie ornare, diam sem sagittis sapien, facilisis dictum ligula velit ut neque. Donec in magna sit amet leo mollis sagittis id sed odio.</p>
      <a class="abs button read-more" href="#" style="left:442px;top:510px">Read more</a>
      <div class="abs share-icons" style="top:536px"><span class="share-feed"></span><span class="share-one"></span><span class="share-two"></span></div>
    </article>
  </section>

  <section class="box ebook" style="left:693px;top:276px;width:294px;height:332px">
    <h2 class="box-title">eBook</h2>
    <p class="abs ebook-quote">"THE CHOICE TO PUT DOWN YOUR GLASS - The Clear Path toward finding calm and keeping it there!"</p>
    <div class="abs ebook-cover" role="img" aria-label="eBook cover artwork"></div>
    <a class="abs button download" href="#">Download now</a>
  </section>

  <section class="box ads" style="left:693px;top:617px;width:294px;height:231px">
    <h2 class="box-title">Ads</h2>
    <div class="abs link-col" style="left:21px;top:68px">
      <h3>Ads by Adverra</h3>
      <a href="#">luctus elementum.</a><a href="#">Vivamus eu</a><a href="#">purus a magna ad</a><a href="#">ipiscing gravida.</a><a href="#">Cras orci nulla.</a>
    </div>
    <div class="abs link-col" style="left:158px;top:68px">
      <h3>Ads by Adverra</h3>
      <a href="#">luctus elementum.</a><a href="#">Vivamus eu</a><a href="#">purus a magna ad</a><a href="#">ipiscing gravida.</a><a href="#">Cras orci nulla.</a>
    </div>
  </section>

  <section class="box links" style="left:693px;top:860px;width:294px;height:231px">
    <h2 class="box-title">Links</h2>
    <div class="abs link-col" style="left:21px;top:66px">
      <h3>Other Blogs</h3>
      <a href="#">luctus elementum.</a><a href="#">Vivamus eu</a><a href="#">purus a magna ad</a><a href="#">ipiscing gravida.</a><a href="#">Cras orci nulla.</a>
    </div>
    <div class="abs link-col" style="left:153px;top:66px">
      <h3>Other Blogs</h3>
      <a href="#">luctus elementum.</a><a href="#">Vivamus eu</a><a href="#">purus a magna ad</a><a href="#">ipiscing gravida.</a><a href="#">Cras orci nulla.</a>
    </div>
  </section>

  <footer class="footer-band"></footer>
</body>
</html>
```